LINGERIE WEBSHOP - Velora casa

We are looking for design and layout design for our webshop. We are company that sells lingerie and other connected textile products liki payamas and etc..
Our website will have approx 500 different products within 2 main catogories Woman/Man) and approx. 10 subcategories
Here is what we expect form design:
-Color pallete should be black and white (if you wish you can add some accent color)
-we want to leave feeling to customers of good quality products towards to luxury
-UX should be simple. Feel free to suggest layout
-frontpage layout, product list layout, product description layout, blog layout
-responsive design, compatible with smartphone

Target Market(s)

woman buying for themself, man buying for woman

Industry/Entity Type

Lingerie

Logo Text

VELORA CASA

Number of Pages Required

4 page

Font styles to use
Sans Serif
Decorative

Requirements
Must have
• simple UX
Nice to have
• difference for sexy/luxury lingerie and daily/cozy lingerie
Should not have
• cheap feel, unreliable

```html
<!DOCTYPE html>
<html lang="hr">
<head>
<meta charset="utf-8">
<title>Velora casa</title>
<link href="https://fonts.googleapis.com/css2?family=Poppins:wght@300;400;500;600;700&display=swap" rel="stylesheet">
<style>
:root{
  --ink:#2b2b2b;
  --black:#000;
  --white:#fff;
  --accent:#5aaef0;
  --mint:#9ff5ec;
  --muted:#777;
  --line:#dcdcdc;
  --panel:#efefef;
  --footer:#333333;
}
*{box-sizing:border-box;margin:0;padding:0}
html,body{width:1200px;height:2636px;overflow:hidden}
body{position:relative;background:var(--white);font-family:'Poppins',sans-serif;color:var(--ink)}
svg{display:block}

/* header */
.site-header{position:absolute;left:0;top:0;width:1200px;height:86px}
.brand{position:absolute;left:0;width:1200px;top:34px;text-align:center;font-size:32px;font-weight:400;letter-spacing:1px;color:var(--black)}
.search{position:absolute;left:880px;top:30px;width:140px;height:26px;border-bottom:1px solid #999;font-size:8px;color:#999;padding:9px 10px}
.search svg{position:absolute;right:0;top:3px}
.wish{position:absolute;left:1036px;top:32px}
.wish .dot{position:absolute;left:12px;top:-2px;width:10px;height:10px;border-radius:50%;background:var(--accent)}
.cart{position:absolute;left:1075px;top:34px;font-size:13px;display:flex;gap:5px;align-items:center}

.main-nav{position:absolute;left:0;top:86px;width:1200px;height:44px;background:var(--black);color:var(--white);font-size:12px;font-weight:500;letter-spacing:.5px}
.main-nav span{position:absolute;top:15px;white-space:nowrap}
.main-nav .on{color:var(--accent)}
.main-nav svg{display:inline-block;vertical-align:middle;margin-left:8px}

/* hero */
.hero{position:absolute;left:0;top:130px;width:1200px;height:439px;background:linear-gradient(90deg,#a8a39f 0%,#8f8a86 40%,#b8aea6 70%,#9c948d 100%)}
.hero-copy{position:absolute;left:140px;width:465px;top:60px;text-align:center;color:var(--white)}
.hero-kicker{font-size:20px;font-weight:700;color:var(--accent);letter-spacing:1px}
.hero-title{font-size:26px;font-weight:400;line-height:53px;margin-top:6px;letter-spacing:1px}
.btn{display:inline-block;background:var(--mint);color:var(--ink);font-size:12px;letter-spacing:.8px;padding:9px 10px;line-height:17px;white-space:nowrap}
.hero .btn{margin-top:28px}
.hero-arrow{position:absolute;top:197px;width:44px;height:44px;border-radius:50%;background:rgba(255,255,255,.75)}
.hero-arrow svg{margin:12px auto}
.dots{position:absolute;display:flex;gap:13px}
.dots i{width:12px;height:12px;border-radius:50%;background:rgba(255,255,255,.55)}
.dots i.on{background:var(--white)}

/* category intro */
.cat-frame{position:absolute;left:262px;top:658px;width:703px;height:263px;border:4px solid #e2e2e2}
.cat-photo{position:absolute;left:235px;top:630px;width:220px;height:220px;background:linear-gradient(135deg,#e8e2df 0%,#c77c76 45%,#b8324e 70%,#d9d2d0 100%)}
.cat-body{position:absolute;left:496px;top:672px;width:430px}
.cat-head{display:flex;align-items:center;gap:18px;font-size:20px;letter-spacing:1px}
.cat-text{font-size:13px;line-height:28px;letter-spacing:.6px;margin-top:18px}
.cat-body .btn{margin-top:22px}
.cat-num{position:absolute;left:900px;top:856px;font-size:42px;font-weight:700;color:#e8e8e8}
.rule{position:absolute;left:72px;width:1056px;height:1px;background:var(--line)}

/* section titles */
.sec-title{position:absolute;left:0;width:1200px;text-align:center;font-size:21px;font-weight:600;letter-spacing:1px;color:var(--ink)}
.sec-title u{text-decoration:none;border-bottom:3px solid var(--accent)}

/* products */
.product{position:absolute;top:1031px;width:176px;text-align:center}
.product .ph{width:176px;height:176px}
.product .name{font-size:12.5px;color:var(--muted);margin-top:14px;letter-spacing:.3px;padding-bottom:4px;white-space:nowrap}
.product .name.on{color:var(--accent);border-bottom:1px solid var(--line)}
.product .price{font-size:13px;margin-top:6px;letter-spacing:.6px}
.prod-actions{position:absolute;left:335px;top:1270px;width:145px;display:flex;justify-content:space-between}
.car-arrow{position:absolute}

/* news */
.post{position:absolute;top:1440px;width:358px}
.post .ph{position:absolute;left:18px;width:323px;height:198px}
.post .date{position:absolute;left:0;top:0;width:70px;height:70px;background:var(--accent);color:var(--white);text-align:center;padding-top:12px}
.post .date b{display:block;font-size:20px;font-weight:700;line-height:22px}
.post .date small{font-size:11px;letter-spacing:1px}
.post .body{position:absolute;left:18px;top:230px;width:323px}
.post h3{font-size:13px;font-weight:600;letter-spacing:.8px;line-height:18px}
.post .meta{display:flex;justify-content:space-between;font-size:10px;color:var(--muted);margin-top:10px}
.post p{font-size:13px;line-height:25px;margin-top:10px;letter-spacing:.2px}
.post .more{display:block;font-size:12px;font-weight:500;margin-top:10px;letter-spacing:.5px}

/* about */
.about{position:absolute;left:0;top:1948px;width:1200px;height:351px;background:var(--panel);text-align:center}
.about h2{font-size:22px;font-weight:600;letter-spacing:1px;margin-top:50px}
.about p{width:960px;margin:22px auto 0;font-size:12.5px;line-height:25px;letter-spacing:.3px;color:#444}
.about h2 + p{margin-top:26px}

/* footer */
.site-footer{position:absolute;left:0;top:2299px;width:1200px;height:310px;background:var(--footer);color:var(--white)}
.foot-brand{position:absolute;left:95px;top:100px;font-size:28px;font-weight:400;letter-spacing:1px}
.socials{position:absolute;left:95px;top:160px;display:flex;gap:24px}
.socials i{width:26px;height:26px;border:1.5px solid var(--white);border-radius:50%}
.foot-col{position:absolute;top:88px;font-size:12px;letter-spacing:.6px;white-space:nowrap}
.foot-col h4{font-size:12px;font-weight:600;margin-bottom:16px}
.foot-col li{list-style:none;line-height:31.5px}
.copy{position:absolute;left:0;top:2609px;width:1200px;height:27px;background:var(--black);color:var(--white);font-size:9px;text-align:center;padding-top:8px;letter-spacing:.3px}
</style>
</head>
<body>

<header class="site-header">
  <div class="brand">VELORA CASA</div>
  <div class="search">SEARCH
    <svg width="20" height="20" viewBox="0 0 20 20"><circle cx="8.5" cy="8.5" r="6.5" fill="none" stroke="#000" stroke-width="1.8"/><line x1="13.3" y1="13.3" x2="18.5" y2="18.5" stroke="#000" stroke-width="1.8"/></svg>
  </div>
  <div class="wish">
    <svg width="20" height="18" viewBox="0 0 20 18"><path d="M10 16.5 2.3 9A4.6 4.6 0 0 1 10 3.3 4.6 4.6 0 0 1 17.7 9Z" fill="none" stroke="#000" stroke-width="1.5"/></svg>
    <span class="dot"></span>
  </div>
  <div class="cart">
    <svg width="18" height="17" viewBox="0 0 18 17"><path d="M1 1h3l2.2 10h9l2-7H5" fill="none" stroke="#000" stroke-width="1.5"/><circle cx="7" cy="14.5" r="1.5"/><circle cx="14" cy="14.5" r="1.5"/></svg>Cart
  </div>
</header>

<nav class="main-nav">
  <span class="on" style="left:307px">NASLOVICA</span>
  <span style="left:432px">ZENE<svg width="12" height="7" viewBox="0 0 12 7"><path d="M1 1l5 5 5-5" fill="none" stroke="#fff"/></svg></span>
  <span style="left:515px">MUSKARCI<svg width="12" height="7" viewBox="0 0 12 7"><path d="M1 1l5 5 5-5" fill="none" stroke="#fff"/></svg></span>
  <span style="left:634px">DJECA<svg width="12" height="7" viewBox="0 0 12 7"><path d="M1 1l5 5 5-5" fill="none" stroke="#fff"/></svg></span>
  <span style="left:728px">O NAMA</span>
  <span style="left:833px">KONTAKT</span>
</nav>

<section class="hero" role="img" aria-label="Fotografija modela u kupaćem kostimu s cvjetnim uzorkom">
  <div class="hero-copy">
    <div class="hero-kicker">KUPAČI KOSTIMI</div>
    <div class="hero-title">ŠIROKI IZBOR ŽENSKIH, MUŠKIH I DJEČJIH KUPAĆIH KOSTIMA IZ NOVE KOLEKCIJE 2019.</div>
    <span class="btn">POGLEDAJTE PROIZVODE</span>
  </div>
  <div class="hero-arrow" style="left:72px"><svg width="20" height="20" viewBox="0 0 20 20"><path d="M13 2 5 10l8 8" fill="none" stroke="#666" stroke-width="1.5"/></svg></div>
  <div class="hero-arrow" style="left:1083px"><svg width="20" height="20" viewBox="0 0 20 20"><path d="M7 2l8 8-8 8" fill="none" stroke="#666" stroke-width="1.5"/></svg></div>
  <div class="dots" style="left:569px;top:392px"><i class="on"></i><i></i><i></i></div>
</section>

<section class="category-intro">
  <svg class="car-arrow" style="left:144px;top:757px" width="22" height="38" viewBox="0 0 22 38"><path d="M20 1 2 19l18 18" fill="none" stroke="#222" stroke-width="1.5"/></svg>
  <svg class="car-arrow" style="left:1036px;top:757px" width="22" height="38" viewBox="0 0 22 38"><path d="M2 1l18 18L2 37" fill="none" stroke="#222" stroke-width="1.5"/></svg>
  <div class="cat-frame"></div>
  <div class="cat-photo" role="img" aria-label="Fotografija modela u crvenom grudnjaku"></div>
  <div class="cat-body">
    <div class="cat-head">
      <svg width="32" height="42" viewBox="0 0 32 42"><circle cx="16" cy="16" r="13" fill="none" stroke="#222" stroke-width="1.4"/><path d="M2 41c1-8 7-11 14-11s13 3 14 11" fill="none" stroke="#222" stroke-width="1.4"/></svg>
      ŽENE
    </div>
    <p class="cat-text">DOLASKOM U VELORA CASA UĆI ĆETE U PREKRASAN SVIJET ŽENSKOG RUBLJA. INTIMNO RUBLJE, NEVIDLJIVO MNOGIM OČIMA, ALI ODUVIJEK BITNO ZA OSOBNO ZADOVOLJSTVO I DOBAR OSJEĆAJ SVAKE ŽENE.</p>
    <span class="btn">POGLEDAJTE PROIZVODE</span>
  </div>
  <div class="cat-num">01</div>
</section>

<div class="rule" style="top:955px"></div>

<section class="featured">
  <h2 class="sec-title" style="top:983px">NAŠI ISTAKNUTI <u>PROIZVODI</u></h2>
  <svg class="car-arrow" style="left:72px;top:1096px" width="24" height="46" viewBox="0 0 24 46"><path d="M22 1 2 23l20 22" fill="none" stroke="#222" stroke-width="1.5"/></svg>
  <svg class="car-arrow" style="left:1104px;top:1096px" width="24" height="46" viewBox="0 0 24 46"><path d="M2 1l20 22L2 45" fill="none" stroke="#222" stroke-width="1.5"/></svg>

  <div class="product" style="left:126px"><div class="ph" role="img" aria-label="Fotografija grudnjaka od čipke boje pudera" style="background:linear-gradient(#f4ece8,#ead8cf)"></div><div class="name">Grundak Lunetta Gem</div><div class="price">229,00 kn</div></div>
  <div class="product" style="left:319px"><div class="ph" role="img" aria-label="Fotografija tamnoplave majice dugih rukava" style="background:linear-gradient(#1d2446,#141a38)"></div><div class="name on">Amarelle Majica 368</div><div class="price">99,00 kn</div></div>
  <div class="product" style="left:512px"><div class="ph" role="img" aria-label="Fotografija crnog čipkastog haltera" style="background:linear-gradient(#f3f3f3,#5a5a5a 40%,#eee 75%)"></div><div class="name">Halter Sorvina 1979</div><div class="price">169,00 kn</div></div>
  <div class="product" style="left:705px"><div class="ph" role="img" aria-label="Fotografija bešavnih gaćica boje kože" style="background:linear-gradient(#f5f3f2,#e9c2a6 60%,#f0ece9)"></div><div class="name">Gacice Liveria 3324</div><div class="price">75,00 kn</div></div>
  <div class="product" style="left:898px"><div class="ph" role="img" aria-label="Fotografija bež oblikujućih hlačica" style="background:linear-gradient(#f2ede3,#e8d9b8)"></div><div class="name">Zenske Hlacice Arvena 108</div><div class="price">89,00 kn</div></div>

  <div class="prod-actions">
    <svg width="20" height="18" viewBox="0 0 20 18"><path d="M10 16.5 2.3 9A4.6 4.6 0 0 1 10 3.3 4.6 4.6 0 0 1 17.7 9Z" fill="none" stroke="#222" stroke-width="1.4"/></svg>
    <svg width="18" height="17" viewBox="0 0 18 17"><path d="M1 1h3l2.2 10h9l2-7H5" fill="none" stroke="#222" stroke-width="1.4"/><circle cx="7" cy="14.5" r="1.5"/><circle cx="14" cy="14.5" r="1.5"/></svg>
  </div>
  <div class="dots" style="left:581px;top:1306px"><i style="background:#222;width:10px;height:10px"></i><i style="background:#bbb;width:10px;height:10px"></i></div>
</section>

<div class="rule" style="top:1350px"></div>

<section class="news">
  <h2 class="sec-title" style="top:1377px;line-height:29px">NAŠE NEDAVNE<br><u>VIJESTI</u></h2>

  <article class="post" style="left:72px">
    <div class="ph" style="top:18px;background:linear-gradient(#6d6a50 0%,#e51f1f 25%,#e03030 75%,#cfc6c0 100%)" role="img" aria-label="Promotivna fotografija akcije s 15% popusta"></div>
    <div class="date"><b>06</b><small>OZU</small></div>
    <div class="body"><h3>POPUST DAN ZENA UZ KOD:<br>15PSTODANZENA</h3><div class="meta"><span>Komentirajte</span><span>Uncategorized</span></div><p>postovani kupci, iskoristite 15% popusta na nasem webshopu i u nasem ducanu u galerija centru povodom Medunarodnog dana zena. popust se odnosi na cijeli asrtiman, cak i na vec snizene artikle i na sve vrste...</p><span class="more">Read More</span></div>
  </article>

  <article class="post" style="left:429px">
    <div class="ph" style="top:16px;background:linear-gradient(#8aa86a 0%,#a6cf60 30%,#b0d466 75%,#c9c2b4 100%)" role="img" aria-label="Promotivna fotografija akcije donjeg rublja na zelenoj pozadini"></div>
    <div class="date" style="top:4px"><b>19</b><small>VELJ</small></div>
    <div class="body"><h3>POPUST DAN ZENA UZ KOD:<br>15PSTODANZENA</h3><div class="meta"><span>Komentirajte</span><span>Uncategorized</span></div><p>postovani kupci, iskoristite 15% popusta na nasem webshopu i u nasem ducanu u galerija centru povodom Medunarodnog dana zena. popust se odnosi na cijeli asrtiman, cak i na vec snizene artikle i na sve vrste...</p><span class="more">Read More</span></div>
  </article>

  <article class="post" style="left:786px">
    <div class="ph" style="top:18px;background:linear-gradient(135deg,#dcc3c5,#e9d3d3 50%,#d8bcbd)" role="img" aria-label="Fotografija ukrasnog srca i ruža na ružičastoj pozadini"></div>
    <div class="date"><b>10</b><small>VELJ</small></div>
    <div class="body"><h3>POPUST DAN ZENA UZ KOD:<br>15PSTODANZENA</h3><div class="meta"><span>Komentirajte</span><span>Uncategorized</span></div><p>postovani kupci, iskoristite 15% popusta na nasem webshopu i u nasem ducanu u galerija centru povodom Medunarodnog dana zena. popust se odnosi na cijeli asrtiman, cak i na vec snizene artikle i na sve vrste...</p><span class="more">Read More</span></div>
  </article>
</section>

<section class="about">
  <h2>VELORA CASA – 20 GODINA S VAMA</h2>
  <p>Na lokaciji najprometnijeg tržnog centra u Zagrebu – Galerija Centru, već 20 godina posluje boutique Velora casa. Trgovina nudi velik izbor omiljenih visokokvalitetnih modnih marki donjeg rublja za žene, muškarce i djecu.</p>
  <p>Novo u ponudi! Nova kolekcija talijanskih čarapa Velatura. Poznati talijanski brend dostupan u Hrvatskoj samo u trgovinama Velora casa. Razni modeli, čvrsto tkanje, moderne boje i dezeni samo su neke od kvaliteta koje nudi Velatura.</p>
  <p>Profinjeno donje rublje, modernih uzoraka i boja, izrađeno od vrhunskih materijala s biranim detaljima nosi nazive Amarelle, Sorvina, Sara Bellini, Lunetta, Lina Baroni, Liveria, Lirena, Mavena, Kalina, Galora, Arvena, Navella, Dianora, Lovely Bloom, Jadora, Moltra, Pomare, Plevia, Velatura.</p>
</section>

<footer class="site-footer">
  <div class="foot-brand">VELORA CASA</div>
  <div class="socials"><i></i><i></i><i></i><i></i><i></i></div>
  <div class="foot-col" style="left:394px"><h4>UPOZNAJTE NAZ</h4><ul><li>UVJETI KORIŠTENJA</li><li>UVJETI KUPNJE</li><li>SIGURNOSNO PLAĆANJE</li></ul></div>
  <div class="foot-col" style="left:672px"><h4>INFORMACIJE</h4><ul><li>NAČINI PLAĆANJA</li><li>DOSTAVA</li><li>POVRATI I ZAMJENE</li></ul></div>
  <div class="foot-col" style="left:907px"><h4>KONTAKT PODACI</h4><ul><li>TEL: 01/5550-123</li><li>MAIL: INFO@VELORACASA.EXAMPLE</li><li>RADNO VRIJEME:</li><li>PON – SUB: 09 – 21 H</li><li>NED: ZATVORENO</li></ul></div>
</footer>
<div class="copy">© 2020 Velora casa. Sva prava pridržana</div>

</body>
</html>
```